Create a banner for a Gmail email signature

We need a graphic design to use in a solicitor's email signature. The banner will incorporate a head shot of the solicitor as well as the law firm's logo and contact details. The solicitor's photo and law firm's logo are uploaded in the task.

```html
<!DOCTYPE html>
<html lang="en">
<head>
<meta charset="utf-8">
<title>Email signature banner options</title>
<link rel="stylesheet" href="https://fonts.googleapis.com/css2?family=Raleway:wght@300;400;500;700&family=Open+Sans:wght@400&family=Arimo:wght@700&display=swap">
<style>
  :root {
    --board: #808080;
    --plum: #850048;
    --plum-glow: #a3005a;
    --ink: #333333;
    --ink-soft: #3c3c3c;
    --paper: #ffffff;
    --paper-fade: #ececec;
    --nav: #8a8a8a;
    --photo-dark: #2b3350;
    --photo-light: #c9b9a6;
  }
  * { box-sizing: border-box; margin: 0; padding: 0; }
  html, body { width: 1200px; height: 933px; overflow: hidden; }
  body {
    position: relative;
    background: var(--board);
    font-family: "Raleway", sans-serif;
    color: var(--ink);
  }
  .option-label {
    position: absolute;
    left: 32px;
    font-family: "Open Sans", sans-serif;
    font-size: 34px;
    color: var(--paper);
    line-height: 1;
  }
  .option-label.first { top: 245px; }
  .option-label.second { top: 631px; }

  .signature {
    position: absolute;
    left: 224px;
    width: 769px;
    box-shadow: 0 22px 22px -14px rgba(0,0,0,.55);
  }
  .signature.classic {
    top: 64px;
    height: 350px;
    background: linear-gradient(90deg, var(--paper) 0%, var(--paper-fade) 100%);
  }
  .signature.portrait {
    top: 486px;
    height: 380px;
    background: var(--paper);
    border: 1px solid #555;
  }
  .nav { position: absolute; top: 5px; right: 43px; display: flex; gap: 9px; }
  .nav svg { width: 18px; height: 18px; display: block; }

  .person-name { font-weight: 700; text-transform: uppercase; }
  .contact-list { list-style: none; }

  .classic .identity { position: absolute; left: 19px; top: 20px; }
  .classic .person-name { font-size: 16px; }
  .classic .role { font-size: 16px; line-height: 20px; }
  .classic .contact-list { position: absolute; left: 19px; top: 92px; font-size: 16px; line-height: 20px; }
  .classic .contact-list li:last-child { margin-top: 3px; }
  .classic .social { position: absolute; left: 17px; top: 184px; }

  .social { display: flex; gap: 4.5px; }
  .social span {
    width: 22px; height: 22px; border-radius: 50%;
    border: 1.3px solid var(--ink);
  }
  .portrait .social span { width: 24px; height: 24px; }
  .portrait .social { gap: 5px; }

  .headshot-round {
    position: absolute; left: 388px; top: 39px;
    width: 110px; height: 110px; border-radius: 50%;
    border: 2px solid var(--plum);
    background: radial-gradient(circle at 55% 40%, var(--photo-light) 0%, #a89479 40%, var(--photo-dark) 85%);
  }
  .classic .rule-vertical {
    position: absolute; left: 505px; top: 43px;
    width: 2px; height: 107px; background: var(--plum);
  }
  .firm-mark {
    position: absolute; left: 515px; top: 69px;
    width: 211px; height: 53px; background: var(--paper);
    display: flex; align-items: center; justify-content: center;
  }
  .firm-mark .firm-name {
    font-size: 19px; font-weight: 400; color: var(--ink); line-height: 1;
  }
  .classic .divider {
    position: absolute; left: 0; right: 0; top: 232px; height: 4px; background: var(--plum);
  }
  .disclaimer {
    position: absolute; left: 12px; right: 12px; top: 253px;
    font-size: 12.6px; line-height: 15px; color: var(--ink-soft);
  }
  .fraud-warning {
    position: absolute; left: 8px; right: 8px; top: 310px;
    font-family: "Arimo", sans-serif; font-weight: 700;
    font-size: 10.9px; line-height: 12.5px; text-align: center; color: var(--ink);
  }

  .headshot-square {
    position: absolute; left: 66px; top: 32px; width: 208px; height: 195px;
    background: linear-gradient(120deg, var(--photo-dark) 0%, #6a6f86 30%, var(--photo-light) 55%, #d8c6b4 70%, #4d5a80 100%);
  }
  .portrait .rule-vertical {
    position: absolute; left: 292px; top: 32px; width: 7px; height: 195px; background: var(--plum);
  }
  .portrait .identity { position: absolute; left: 319px; top: 31px; }
  .portrait .person-name { font-size: 26px; color: var(--plum); line-height: 30px; }
  .portrait .role { font-size: 22px; line-height: 26px; }
  .portrait .contact-list { position: absolute; left: 319px; top: 99px; font-size: 17.5px; line-height: 21px; }
  .portrait .contact-list li:last-child { margin-top: 4px; }
  .portrait .social { position: absolute; left: 318px; top: 200px; }

  .cta-band {
    position: absolute; left: 0; right: 0; bottom: 0; height: 106px;
    background: var(--plum); overflow: hidden;
  }
  .cta-band .glow {
    position: absolute; left: 240px; top: 0; width: 104px; height: 104px; border-radius: 50%;
    background: radial-gradient(circle, var(--plum-glow) 0%, var(--plum-glow) 55%, #8f004e 56%, #8f004e 100%);
    opacity: .9;
  }
  .cta-band .notch { position: absolute; left: 268px; top: -1px; width: 48px; height: 25px; }
  .cta-text {
    position: absolute; left: 189px; top: 33px;
    font-size: 27px; font-weight: 300; color: var(--paper); letter-spacing: .3px;
    white-space: nowrap;
  }
  .cta-text strong { font-weight: 700; margin: 0 6px; }
</style>
</head>
<body>

  <p class="option-label first">option-1</p>
  <p class="option-label second">option-2</p>

  <section class="signature classic" aria-label="Signature option one">
    <div class="nav" aria-hidden="true">
      <svg viewBox="0 0 18 18"><circle cx="9" cy="9" r="9" fill="var(--nav)"/><path d="M10.5 5 6.5 9l4 4" fill="none" stroke="#fff" stroke-width="1.4"/></svg>
      <svg viewBox="0 0 18 18"><circle cx="9" cy="9" r="9" fill="var(--nav)"/><path d="M7.5 5l4 4-4 4" fill="none" stroke="#fff" stroke-width="1.4"/></svg>
    </div>
    <div class="identity">
      <p class="person-name">Name here</p>
      <p class="role">legal Advisor</p>
    </div>
    <ul class="contact-list">
      <li>01632 960418</li>
      <li>0207 946 0321</li>
      <li>name@harbourlinelegal.com</li>
      <li>www.harbourlinelegal.com</li>
    </ul>
    <div class="social" aria-label="Social links"><span></span><span></span><span></span><span></span><span></span><span></span></div>
    <div class="headshot-round" role="img" aria-label="Head shot of the solicitor"></div>
    <div class="rule-vertical"></div>
    <div class="firm-mark">
      <span class="firm-name">Harbourline Legal</span>
    </div>
    <div class="divider"></div>
    <p class="disclaimer">Lorem ipsum, or lipsum as it is sometimes known, is dummy text used in laying out print, graphic or web designs. The passage is attributed to an unknown typesetter in the 15th century who is thought to have scrambled parts of Cicero's De Finibus Bonor um et Malorum for use in a type specimen book.</p>
    <p class="fraud-warning">WARNING: EMAIL FRAUD. WE WILL NEVER PROVIDE YOU WITH OUR BANK DETAILS BY E-MAIL. YOU MUST ALWAYS VERIFY OUR BANK DETAILS DIRECTLY WITH US BEFORE MAKING TRANSFERS**</p>
  </section>

  <section class="signature portrait" aria-label="Signature option two">
    <div class="nav" aria-hidden="true">
      <svg viewBox="0 0 18 18"><circle cx="9" cy="9" r="9" fill="var(--nav)"/><path d="M10.5 5 6.5 9l4 4" fill="none" stroke="#fff" stroke-width="1.4"/></svg>
      <svg viewBox="0 0 18 18"><circle cx="9" cy="9" r="9" fill="var(--nav)"/><path d="M7.5 5l4 4-4 4" fill="none" stroke="#fff" stroke-width="1.4"/></svg>
    </div>
    <div class="headshot-square" role="img" aria-label="Head shot of the solicitor"></div>
    <div class="rule-vertical"></div>
    <div class="identity">
      <p class="person-name">Maren</p>
      <p class="role">legal Advisor</p>
    </div>
    <ul class="contact-list">
      <li>01632 960418</li>
      <li>0207 946 0321</li>
      <li>name@harbourlinelegal.com</li>
      <li>www.harbourlinelegal.com</li>
    </ul>
    <div class="social" aria-label="Social links"><span></span><span></span><span></span><span></span><span></span><span></span></div>
    <div class="cta-band">
      <div class="glow"></div>
      <svg class="notch" viewBox="0 0 48 25" aria-hidden="true"><path d="M0 0h48L27 22.5q-3 3-6 0z" fill="var(--paper)"/></svg>
      <p class="cta-text">Click <strong>here</strong> to learn more</p>
    </div>
  </section>

</body>
</html>
```